Trade Show Banner "Brindlequay"

1.7' x 3' vertical banner to complement trade show booth panels (3-panel tabletop booth attached). The word file (attached) is for text and not meant to imply design. We manage homeowner and condo associations that are run by volunteer boards of directors who already have full-time jobs or who may have no training in how to run an organization. It can be highly stressful and not very rewarding. We want this poster/banner to convey that feeling of stress along with a hope for relief and relaxation. Our logo is attached. The full logo is the top one in the file. You may also want to use the triangle (attached) in addition to or instead of the logo. Our corporate fonts are attached. Please let me know if you need additional information or if you feel like there is too much copy or any other thoughts or comments you have.

Target Market(s)

Volunteer boards of directors for homeowner and condo associations--all ages, genders, races, occupations.

Industry/Entity Type

Property Management

Other font styles liked:
• "Copper Lantern" is part of a trademark and should be in Mistral with the green from our logo

Requirements
Must have
• Simple, easy to read, don't clash with booth design
Nice to have
• convey the tension of stress contrasted with the feeling of relaxation and relief.

```html
<!DOCTYPE html>
<html lang="en">
<head>
<meta charset="utf-8">
<title>Brindlequay – For Board Members</title>
<link rel="stylesheet" href="https://fonts.googleapis.com/css2?family=Fira+Sans+Condensed:wght@500;600&family=PT+Sans:ital,wght@0,400;0,700;1,700&family=Kaushan+Script&display=swap">
<style>
  :root {
    --navy: #1f2a6b;
    --maroon: #6b1420;
    --green: #1e7a3c;
    --ink: #2a2a2a;
    --paper: #ffffff;
    --frame: #3a3a3a;
  }
  * { margin: 0; padding: 0; box-sizing: border-box; }
  html, body { width: 680px; height: 1200px; overflow: hidden; background: var(--paper); }
  .banner {
    position: relative;
    width: 680px;
    height: 1200px;
    border: 1px solid var(--frame);
    background: var(--paper);
  }
  .brand {
    height: 179px;
    display: flex;
    align-items: center;
    justify-content: center;
    gap: 14px;
    border-bottom: 1px solid var(--frame);
  }
  .brand-square { width: 26px; height: 26px; background: var(--navy); }
  .brand-name {
    font-family: "Fira Sans Condensed", sans-serif;
    font-weight: 600;
    font-size: 46px;
    color: var(--navy);
    letter-spacing: 1px;
  }
  .hero {
    position: relative;
    height: 347px;
    border-bottom: 1px solid var(--frame);
  }
  .hero-photo {
    position: absolute;
    inset: 0;
    background:
      radial-gradient(ellipse at 55% 55%, #e6b99c 0%, #c98e6e 30%, transparent 60%),
      linear-gradient(180deg, #4a2c1a 0%, #7a4a2c 45%, #d8c7a8 80%, #c9ab84 100%);
  }
  .badge {
    position: absolute;
    left: 12px;
    top: 192px;
    top: 13px;
    width: 260px;
    height: 120px;
  }
  .badge svg { position: absolute; inset: 0; }
  .badge-text {
    position: absolute;
    inset: 0;
    display: flex;
    flex-direction: column;
    align-items: center;
    justify-content: center;
    font-family: "Fira Sans Condensed", sans-serif;
    font-weight: 600;
    font-size: 30px;
    line-height: 30px;
    color: var(--paper);
    text-align: center;
  }
  .message {
    position: absolute;
    left: 18px;
    right: 18px;
    top: 538px;
  }
  .stress {
    font-family: "Fira Sans Condensed", sans-serif;
    font-weight: 500;
    font-size: 29px;
    line-height: 36px;
    color: var(--navy);
    white-space: nowrap;
  }
  .relief {
    font-family: "PT Sans", sans-serif;
    font-size: 28px;
    line-height: 34px;
    color: var(--ink);
    padding-left: 110px;
    text-indent: -110px;
    margin-bottom: 6px;
  }
  .relief.justified { text-align: justify; }
  .relax {
    font-weight: 700;
    font-style: italic;
    color: var(--maroon);
  }
  .trademark {
    font-family: "Kaushan Script", cursive;
    color: var(--green);
    font-size: 27px;
  }
  .closing {
    position: absolute;
    left: 0;
    right: 0;
    top: 1150px;
    text-align: center;
    font-family: "PT Sans", sans-serif;
    font-weight: 700;
    font-style: italic;
    font-size: 30px;
    color: var(--maroon);
  }
</style>
</head>
<body>
<main class="banner">
  <header class="brand">
    <span class="brand-square"></span>
    <span class="brand-name">Brindlequay</span>
  </header>

  <section class="hero">
    <div class="hero-photo" role="img" aria-label="Photo of a woman relaxing face down on a towel while receiving a shoulder massage in a warm spa setting"></div>
    <div class="badge">
      <svg viewBox="0 0 260 120" width="260" height="120">
        <polygon fill="#1e7a3c" stroke="#ffffff" stroke-width="2"
          points="260,60 236,69 250,83 220,86 222,102 190,98 180,115 151,105 130,120 109,105 80,115 70,98 38,102 40,86 10,83 24,69 0,60 24,51 10,37 40,34 38,18 70,22 80,5 109,15 130,0 151,15 180,5 190,22 222,18 220,34 250,37 236,51"/>
      </svg>
      <div class="badge-text"><span>FOR BOARD</span><span>MEMBERS</span></div>
    </div>
  </section>

  <section class="message">
    <p class="stress">Stress: THE BOARD HAS TOO MUCH WORK TO DO</p>
    <p class="relief"><span class="relax">Relax…</span>and let us do the work.</p>

    <p class="stress">Stress: YOUR COMMUNITY HAS “ISSUES.”</p>
    <p class="relief"><span class="relax">Relax…</span>and let us give you a <span class="trademark">Copper Lantern</span>.</p>

    <p class="stress">Stress: YOUR MEMBERS CANNOT PAY ONLINE.</p>
    <p class="relief justified"><span class="relax">Relax…</span>we’ll give your members multiple ways to pay.</p>

    <p class="stress">Stress: COMMUNICATION IS POOR OR INCONSISTENT.</p>
    <p class="relief justified"><span class="relax">Relax…</span>we’ll keep you informed with a robust online portal, chock full of information.</p>

    <p class="stress">Stress: YOUR DELINQUENCIES ARE HIGH.</p>
    <p class="relief justified"><span class="relax">Relax…</span>as a licensed collection agency, we have developed an effective collections program that works in tandem with your collections attorney. Plus, we can report to the credit bureau!</p>
  </section>

  <p class="closing">COME IN TO TALK AND START RELAXING TODAY!</p>
</main>
</body>
</html>
```